Postcard: Live Ever Kinder

Text for front: HOW TO CHANGE THE WORLD IN ONE [note: the word "one" should be underlined] STEPHint: It's up to you...[Note: add arrow or something to indicate "turn over"]Text for back: You're going to spend your entire life with someone you can never get away from. (Guess who?) Wouldn't you rather that person #LiveEverKinder than judgmental or critical? BE the change you want to see! Visit www.LiveEverKinder-hub.com for daily Bright Pebbles and community. PLEASE JOIN US![Note: add logo to left half of back side]Font preference for text: Josefin sans

Target Market(s)

People who would be attracted to Calvera church - unitarian universalist message. It's spiritual without being overtly religious, so the target market is probably early 30s and up but ideally won't turn off Millennials (folks under 30). It should attract attention of people who are open-minded and committed to progressive social change, tired of an atmosphere of hate-mongering and divisiveness.

Requirements
Nice to have
• It would be nice to convey a sense of challenge - there is an idea of "bright pebbles" so something related to fire/sparks is appropriate. This is meant to evoke a deeper, divine love more than a sense of romantic love. This love is more fierce than fluffy! Yet it calls us to be our best selves.
Should not have
• Please avoid excessive pink - just the logo is enough, as this design needs to appeal to men as well as women.

```html
<!DOCTYPE html>
<html lang="en">
<head>
<meta charset="utf-8">
<title>Live Ever Kinder – Postcard</title>
<link rel="stylesheet" href="https://fonts.googleapis.com/css2?family=Bebas+Neue&family=Josefin+Sans:wght@300;400&family=Satisfy&display=swap">
<style>
  :root {
    --backdrop: #e9e4dc;
    --sky-blue: #4aaef2;
    --band-blue: #4fb4f5;
    --arrow-blue: #2e6be0;
    --ink: #111111;
    --white: #ffffff;
    --text-dark: #222222;
    --accent-blue: #3aa6f0;
    --logo-pink: #ec4fa6;
  }
  * { margin: 0; padding: 0; box-sizing: border-box; }
  html, body { width: 1200px; height: 444px; overflow: hidden; }
  body { background: var(--backdrop); position: relative; }

  .card { position: absolute; top: 37px; height: 378px; overflow: hidden; }

  /* Front */
  .card-front { left: 33px; width: 535px; background: var(--sky-blue); }
  .front-photo {
    position: absolute; left: 302px; top: 0; width: 233px; height: 100%;
    background: linear-gradient(180deg, #c45d8c 0%, #b8877a 25%, #d8a995 55%, #6e7b3f 85%, #4f5d2c 100%);
  }
  .headline {
    position: absolute; left: 17px; top: 30px;
    font-family: "Bebas Neue", "Oswald", sans-serif; color: var(--ink);
    line-height: 1;
  }
  .headline-line { display: block; font-size: 66px; letter-spacing: 0.5px; height: 64px; }
  .headline-line--big { font-size: 90px; height: 90px; margin-top: 4px; }
  .headline-emphasis {
    color: var(--white);
    text-decoration: underline; text-decoration-thickness: 6px; text-underline-offset: 4px;
  }
  .turn-arrow { position: absolute; left: 0; top: 262px; width: 535px; height: 116px; }
  .hint {
    position: absolute; left: 30px; top: 296px;
    font-family: "Satisfy", cursive; font-size: 36px; color: var(--white);
    letter-spacing: 0.5px;
  }

  /* Back */
  .card-back { left: 585px; width: 585px; background: var(--white); }
  .logo {
    position: absolute; left: 62px; top: 30px; width: 170px; height: 170px;
    display: flex; align-items: center; justify-content: center;
  }
  .logo-mark {
    position: absolute; inset: 0; border-radius: 50%; background: var(--logo-pink);
  }
  .logo-name {
    position: relative; font-family: "Josefin Sans", sans-serif; font-weight: 400;
    font-size: 22px; color: var(--white); text-align: center; line-height: 1.2;
  }
  .butterflies {
    position: absolute; left: 205px; top: 5px; width: 100px; height: 295px;
    background: linear-gradient(180deg, rgba(170,170,245,0.45), rgba(200,200,250,0.15));
    border-radius: 40px;
  }
  .message {
    position: absolute; left: 308px; top: 34px; width: 270px;
    font-family: "Josefin Sans", sans-serif; font-weight: 400;
    font-size: 15px; line-height: 17.5px; color: var(--text-dark);
  }
  .message p { margin-bottom: 3px; }
  .accent { color: var(--accent-blue); }
  .visit { text-align: center; margin-top: 12px; width: 240px; }
  .join-band {
    position: absolute; left: 0; top: 281px; width: 100%; height: 52px;
    background: var(--band-blue);
    font-family: "Josefin Sans", sans-serif; font-weight: 300;
    font-size: 37px; letter-spacing: 2px; color: var(--white);
    display: flex; align-items: center; justify-content: center; padding-top: 6px;
  }
</style>
</head>
<body>

<section class="card card-front">
  <div class="front-photo" role="img" aria-label="Photo of bare feet on grass with the words 'We can change the world' written on the soles"></div>
  <h1 class="headline">
    <span class="headline-line">How to change</span>
    <span class="headline-line">the world in</span>
    <span class="headline-line headline-line--big"><span class="headline-emphasis">One</span> step</span>
  </h1>
  <svg class="turn-arrow" viewBox="0 0 535 116" aria-hidden="true">
    <polygon points="12,50 475,50 475,35 527,96 475,155 475,140 12,140" fill="var(--arrow-blue)" transform="translate(0,-25)"/>
  </svg>
  <p class="hint">Hint: It's Up to You . . .</p>
</section>

<section class="card card-back">
  <div class="logo">
    <span class="logo-mark"></span>
    <span class="logo-name">Live Ever<br>Kinder</span>
  </div>
  <div class="butterflies" role="img" aria-label="Illustration of pale lavender butterflies"></div>
  <div class="message">
    <p>You are going to spend<br>your entire life with<br>someone you can never<br>get away from.</p>
    <p class="accent">GUESS WHO?</p>
    <p>Wouldn't you rather that<br>person #LiveEverKinder<br>than judgmental or critical?<br><span class="accent">BE</span> the change you want to see!</p>
    <p class="visit">Visit:<br><span class="accent">www.LiveEverKinder-hub.com</span><br>daily bright pebbles and community</p>
  </div>
  <div class="join-band">PLEASE JOIN US</div>
</section>

</body>
</html>
```